Business Card Design for retail pharmacist based in Sydney, Australia

I need a professional, health care oriented business card for a reatil pharmacist providing health advice and information

```html
<!DOCTYPE html>
<html lang="en">
<head>
<meta charset="utf-8">
<title>Daniel Marchetti – Business Card</title>
<link rel="stylesheet" href="https://fonts.googleapis.com/css2?family=Nunito+Sans:wght@700&family=Questrial&display=swap">
<style>
  :root {
    --page-bg: #e6e4e1;
    --card-top: #ffffff;
    --card-bottom: #ececec;
    --accent-orange: #f5a020;
    --accent-orange-deep: #ee9414;
    --ink: #474747;
  }
  html, body {
    margin: 0;
    padding: 0;
    width: 1200px;
    height: 825px;
    overflow: hidden;
    background: var(--page-bg);
  }
  .canvas {
    position: relative;
    width: 1200px;
    height: 825px;
  }
  .business-card {
    position: absolute;
    left: 120px;
    top: 118px;
    width: 960px;
    height: 590px;
    border-radius: 24px;
    overflow: hidden;
    background: linear-gradient(180deg, var(--card-top) 0%, var(--card-bottom) 100%);
    box-shadow: 0 4px 14px rgba(0, 0, 0, 0.12);
  }
  .illustration-area {
    position: absolute;
    left: 0;
    right: 0;
    bottom: 0;
    height: 330px;
  }
  .illustration-area .skyline-strip {
    position: absolute;
    left: 0;
    right: 0;
    bottom: 0;
    height: 60px;
    background: linear-gradient(90deg, var(--accent-orange) 0%, var(--accent-orange-deep) 100%);
  }
  .illustration-area .apothecary-block {
    position: absolute;
    right: 0;
    bottom: 0;
    width: 330px;
    height: 330px;
    background: linear-gradient(180deg, var(--accent-orange) 0%, var(--accent-orange-deep) 100%);
  }
  .identity {
    position: absolute;
    right: 48px;
    top: 66px;
    text-align: right;
    color: var(--ink);
  }
  .identity .person-name {
    margin: 0;
    font-family: "Nunito Sans", sans-serif;
    font-weight: 700;
    font-size: 54px;
    line-height: 1.1;
  }
  .identity .credentials {
    margin: 8px 0 0;
    font-family: "Questrial", sans-serif;
    font-size: 28px;
  }
  .contact-list {
    position: absolute;
    left: 38px;
    top: 336px;
    margin: 0;
    padding: 0;
    list-style: none;
    font-family: "Questrial", sans-serif;
    font-size: 27px;
    line-height: 38px;
    color: var(--ink);
  }
</style>
</head>
<body>
  <div class="canvas">
    <div class="business-card">
      <div class="illustration-area" role="img"
           aria-label="Orange silhouette illustration: Sydney skyline with harbour bridge along the bottom, rising on the right into a large mortar and pestle">
        <div class="skyline-strip"></div>
        <div class="apothecary-block"></div>
      </div>

      <header class="identity">
        <h1 class="person-name">Daniel Marchetti</h1>
        <p class="credentials">B. Pharm (Hons I, Uni Medal), MPS</p>
      </header>

      <ul class="contact-list">
        <li class="contact-email">info@harbourchemist.com.au</li>
        <li class="contact-mobile">0412 555 018</li>
        <li class="contact-store">02 9555 0143 (Bayside Pharmacy)</li>
        <li class="contact-store">02 9555 0276 (Hillcrest Pharmacy)</li>
      </ul>
    </div>
  </div>
</body>
</html>
```